Velno - Website for fruit & juice

- The location of the outlet is Fort Kochi in India.
- Fort Kochi is a tourist destination. And it attracts majorly French and Portuguese tourist due to the history of the place.
- The location had plenty of food joints & mostly provide local foods only without giving much options to tourist.
- Road side fruit shops don't look hygienic
- At Velno we are going to sell fresh fruits as well as fruit juices.
- Customers can pick their fruits and Velno staffs will squeeze/blend or slice it for them.
- There will be no e-commerce on the site (no buying of products through site)

Target Market(s)

Tourist & health conscious individuals who want to have fresh fruit or juice.

Coding

Coded - Design and coding required

Number of Pages Required

4 page

Font styles to use
Script

Colors

Designer to choose colors to be used in the design.

Requirements
Must have
• Back End. Editable website.
• Since it for fruits & juices, we will be selling fruits as per season or availability.
• Editable or back end will allow us to add or delete menus as per availability.
• The project much have 4 pages. Namely:
• - Home
• - Concept
• - Menu
• - Location & Contact
Nice to have
• Fresh feel of the website
Should not have
• E-commerce

```html
<!DOCTYPE html>
<html lang="en">
<head>
<meta charset="utf-8">
<title>Velno – Fresh Fruits &amp; Fresh Juices</title>
<link href="https://fonts.googleapis.com/css2?family=Kaushan+Script&family=Montserrat:wght@400;600;700&family=PT+Serif:ital@0;1&display=swap" rel="stylesheet">
<style>
:root{
  --green:#3e7a57;
  --green-dark:#2f6446;
  --lime:#8cc63f;
  --orange:#f39a1e;
  --yellow:#f6c700;
  --ink:#2b2b2b;
  --muted:#8a8a8a;
  --panel:#f3f3f1;
  --band:#f1f1ef;
  --white:#ffffff;
}
*{box-sizing:border-box;margin:0;padding:0}
html,body{width:1200px;height:5202px;overflow:hidden;background:var(--white)}
body{position:relative;font-family:"PT Serif",Georgia,serif;color:var(--ink)}
.abs{position:absolute}
.sans{font-family:"Montserrat",Arial,sans-serif}

/* top bar & header */
.topbar{left:0;top:0;width:1200px;height:28px;background:#f3f3f3;font-size:11px;color:var(--muted)}
.topbar .addr{left:62px;top:8px}
.topbar .call{right:55px;top:8px}
.topbar .call b{color:var(--ink)}
.brand{color:var(--green);font-family:"Montserrat",Arial,sans-serif;font-weight:700;font-size:30px;line-height:1}
.header .brand{left:55px;top:74px}
.nav{top:78px;right:55px;display:flex;gap:38px;font-family:"Montserrat",Arial,sans-serif;font-size:14px;color:var(--ink)}
.nav .active{color:var(--orange)}

/* hero */
.hero-photo{left:0;top:140px;width:614px;height:495px;background:linear-gradient(120deg,#7aa23a 0%,#e7b021 30%,#e23b2a 55%,#b3241c 75%,#5b8a2c 100%)}
.hero-panel{left:614px;top:140px;width:586px;height:495px;background:var(--green)}
.hero-kicker{left:692px;top:282px;color:var(--white);font-family:"Montserrat",Arial,sans-serif;font-size:15px;letter-spacing:8px;font-style:italic}
.hero-title{left:692px;top:306px;color:var(--white);font-family:"Kaushan Script",cursive;font-weight:400;font-size:52px;line-height:60px;width:420px}
.hero-title .amp{color:var(--orange);position:absolute;left:355px;top:28px;font-size:58px}
.hero-more{left:692px;top:448px;color:var(--white);font-family:"Montserrat",Arial,sans-serif;font-size:12px;letter-spacing:6px}

/* section headings */
.heading{left:0;width:1200px;text-align:center;font-family:"Montserrat",Arial,sans-serif;font-weight:700;font-size:40px;color:var(--ink)}
.heading.script{font-family:"Kaushan Script",cursive;font-weight:400;font-size:50px}
.rule{left:570px;width:60px;height:3px;background:var(--lime)}
.sub{left:0;width:1200px;text-align:center;font-style:italic;font-size:15px;color:var(--muted)}

/* feature cards */
.feature{width:277px;height:506px;top:840px;background:var(--panel);text-align:center}
.feature .icon{position:absolute;left:66px;top:41px;width:146px;height:146px;border-radius:50%}
.feature h3{position:absolute;left:0;width:100%;top:222px;font-family:"Montserrat",Arial,sans-serif;font-size:27px;font-weight:700}
.feature p{position:absolute;left:38px;width:201px;top:280px;font-size:13px;line-height:23px;color:var(--muted)}
.btn-outline{display:inline-block;border:2px solid var(--lime);color:var(--lime);border-radius:20px;font-family:"Montserrat",Arial,sans-serif;font-weight:700;font-size:11px;letter-spacing:1px}
.feature .btn-outline{position:absolute;left:96px;top:418px;width:86px;height:34px;line-height:30px}

/* fruits band */
.band{left:0;top:1432px;width:1200px;height:625px;background:var(--band)}
.fruit{top:1620px;width:302px;height:364px;background:var(--white)}
.fruit .art{position:absolute;left:56px;top:36px;width:190px;height:190px;border-radius:10px}
.fruit .name{position:absolute;left:0;width:100%;top:272px;text-align:center;font-family:"Kaushan Script",cursive;font-size:24px}
.dots{top:2006px;left:584px;display:flex;gap:10px}
.dots span{width:9px;height:9px;border-radius:50%;background:var(--ink)}
.dots span.on{background:var(--orange)}

/* juices */
.juice{width:272px;height:434px;background:var(--panel)}
.juice .art{position:absolute;left:56px;top:40px;width:160px;height:240px;border-radius:10px}
.juice .name{position:absolute;left:0;width:100%;top:330px;text-align:center;font-family:"Kaushan Script",cursive;font-size:23px}
.btn-solid{left:489px;top:3258px;width:222px;height:46px;line-height:46px;border-radius:24px;background:var(--lime);color:var(--white);text-align:center;font-family:"Montserrat",Arial,sans-serif;font-weight:700;font-size:13px;letter-spacing:1px}

/* articles */
.article{top:3600px;width:276px;height:510px;background:var(--panel);text-align:center}
.article .art{position:absolute;left:0;top:0;width:276px;height:277px}
.article h4{position:absolute;left:0;width:100%;top:310px;font-family:"Montserrat",Arial,sans-serif;font-size:20px;font-weight:700}
.article .date{position:absolute;left:0;width:100%;top:352px;font-size:12px;color:var(--muted)}
.article .meta{position:absolute;left:0;width:100%;top:380px;font-size:11px;color:var(--muted)}
.article .meta i{font-style:normal;color:var(--lime)}
.article .btn-outline{position:absolute;left:63px;top:426px;width:150px;height:34px;line-height:30px}

/* newsletter */
.news{left:49px;top:4224px;width:1102px;height:285px;background:var(--green)}
.news h2{position:absolute;left:0;width:100%;top:68px;text-align:center;color:var(--white);font-family:"Montserrat",Arial,sans-serif;font-weight:700;font-size:38px}
.news .field{position:absolute;left:395px;top:140px;width:200px;height:46px;border-radius:24px 0 0 24px;background:var(--white);padding-left:24px;line-height:46px;font-size:13px;color:var(--muted)}
.news .submit{position:absolute;left:595px;top:140px;width:162px;height:46px;border-radius:0 24px 24px 0;background:#c9a322;color:var(--white);text-align:center;line-height:46px;font-family:"Montserrat",Arial,sans-serif;font-weight:700;font-size:13px}
.news .terms{position:absolute;left:410px;top:200px;color:var(--white);font-size:11px;display:flex;gap:8px;align-items:center}
.news .terms span{width:11px;height:11px;background:var(--white)}
.map{left:49px;top:4509px;width:1102px;height:260px;background:linear-gradient(135deg,#e9ecef,#dfe5e0 50%,#e6e8ec)}

/* footer */
.footer .brand{left:160px;top:4852px}
.footer-about{left:160px;top:4918px;width:245px;font-size:12px;line-height:21px;color:var(--muted)}
.col-title{font-family:"Montserrat",Arial,sans-serif;font-weight:700;font-size:18px;top:4852px}
.col-list{top:4910px;font-size:12px;line-height:21px;color:var(--muted);list-style:none}
.contact{left:818px;top:4910px;font-size:12px;line-height:21px;color:var(--muted)}
.contact .ico{color:var(--lime);margin-right:6px}
.social{left:818px;top:4990px;display:flex;gap:7px}
.social span{width:22px;height:22px;border-radius:50%;border:2px solid var(--lime)}
.copy{left:0;width:1200px;top:5160px;text-align:center;font-size:11px;color:var(--ink)}
.to-top{left:1127px;top:5136px;width:45px;height:45px;background:var(--lime)}
</style>
</head>
<body>

<div class="abs topbar">
  <span class="abs addr">14, Rosewood Lane, Harbor Bay, KL 68201</span>
  <span class="abs call">Call Us for Ordering <b>555-210-4477</b></span>
</div>

<header class="header">
  <div class="abs brand">Velno</div>
  <nav class="abs nav"><span class="active">Home</span><span>Concept</span><span>Menu</span><span>Location &amp; Contact</span></nav>
</header>

<section class="hero">
  <div class="abs hero-photo" role="img" aria-label="Glasses of green, orange and red juices with fresh guava, strawberries and kiwi"></div>
  <div class="abs hero-panel"></div>
  <div class="abs hero-kicker">VELNO</div>
  <h1 class="abs hero-title">Fresh Fruits<br>Fresh Juices<span class="amp">&amp;</span></h1>
  <div class="abs hero-more">READ MORE</div>
</section>

<section class="different">
  <h2 class="abs heading" style="top:684px">What Makes Us Different</h2>
  <div class="abs rule" style="top:752px"></div>
  <p class="abs sub" style="top:772px">We Are Really Good</p>

  <article class="abs feature" style="left:160px">
    <div class="icon" style="background:var(--green-dark)" role="img" aria-label="Juice jar icon"></div>
    <h3>Organic.</h3>
    <p>We make our juices raw, alive and full of vitamins, minerals and essential nutrients. It never gets heated or high-pressurized, 100% fresh.</p>
    <span class="btn-outline">MORE</span>
  </article>
  <article class="abs feature" style="left:461px">
    <div class="icon" style="background:var(--lime)" role="img" aria-label="Kiwi slice icon"></div>
    <h3>Natural.</h3>
    <p>Every juice is filled with two pounds of organic fruits and vegetables, freshly pressed daily, that proves items of using and keeping.</p>
    <span class="btn-outline">MORE</span>
  </article>
  <article class="abs feature" style="left:763px">
    <div class="icon" style="background:var(--yellow)">
      <svg width="146" height="146" viewBox="0 0 146 146"><path d="M73 96 C50 80 46 66 52 58 C58 50 68 52 73 60 C78 52 88 50 94 58 C100 66 96 80 73 96Z" fill="var(--green)"/></svg>
    </div>
    <h3>Healthy.</h3>
    <p>Your body deserves the best vitamins and drinks. We provide only top quality products based on organic materials. Live long and healthy.</p>
    <span class="btn-outline">MORE</span>
  </article>
</section>

<section class="fruits">
  <div class="abs band"></div>
  <h2 class="abs heading script" style="top:1478px">Fruits</h2>
  <p class="abs sub sans" style="top:1546px;font-size:11px;font-style:normal;color:var(--ink)">What is new ?</p>

  <div class="abs fruit" style="left:160px"><div class="art" style="background:radial-gradient(circle,#f2c230,#c88a1e 60%,#6f8c2c)" role="img" aria-label="Pineapple with slices"></div><div class="name">Pineapple</div></div>
  <div class="abs fruit" style="left:482px"><div class="art" style="background:radial-gradient(circle,#d8283b,#a11829 70%,#e6d0c4)" role="img" aria-label="Pomegranate halves and seeds"></div><div class="name">Pomegranate</div></div>
  <div class="abs fruit" style="left:815px"><div class="art" style="background:radial-gradient(circle,#f6a21c,#e6820e 65%,#7aa33a)" role="img" aria-label="Oranges with leaves"></div><div class="name">Orange</div></div>
  <div class="abs dots"><span></span><span class="on"></span><span></span></div>
</section>

<section class="juices">
  <h2 class="abs heading script" style="top:2140px">Juices &amp; Smoothies</h2>
  <p class="abs sub" style="top:2218px">What's New?</p>

  <div class="abs juice" style="left:160px;top:2289px"><div class="art" style="background:linear-gradient(180deg,#f9c07a,#f07d16)" role="img" aria-label="Carrot juice with carrots"></div><div class="name">Carrot juice</div></div>
  <div class="abs juice" style="left:458px;top:2289px"><div class="art" style="background:linear-gradient(180deg,#e3576a,#b51d2e)" role="img" aria-label="Pomegranate juice with fruit"></div><div class="name">Pomegranate juice</div></div>
  <div class="abs juice" style="left:760px;top:2289px"><div class="art" style="background:linear-gradient(180deg,#fbe68a,#f3c21a)" role="img" aria-label="Pineapple juice with pineapple"></div><div class="name">Pinaple Juice</div></div>
  <div class="abs juice" style="left:160px;top:2764px"><div class="art" style="background:linear-gradient(180deg,#a9d36a,#4d8a2a)" role="img" aria-label="Kiwi juice with kiwi slices"></div><div class="name">Kiwi juice</div></div>
  <div class="abs juice" style="left:458px;top:2764px"><div class="art" style="background:linear-gradient(180deg,#8a5a8e,#3f2240)" role="img" aria-label="Grape juice with grapes"></div><div class="name">Grapes juice</div></div>
  <div class="abs juice" style="left:760px;top:2764px"><div class="art" style="background:linear-gradient(180deg,#fbe68a,#f3c21a)" role="img" aria-label="Pineapple juice with pineapple"></div><div class="name">Pinaple Juice</div></div>

  <div class="abs btn-solid">VIEW MORE PRODUCTS</div>
</section>

<section class="articles">
  <h2 class="abs heading" style="top:3442px">Recent Articles</h2>
  <div class="abs rule" style="top:3510px"></div>
  <p class="abs sub" style="top:3533px">Learn About Some Useful Facts</p>

  <article class="abs article" style="left:160px"><div class="art" style="background:linear-gradient(135deg,#c9d6e8,#eae3d8 50%,#c85a4a)" role="img" aria-label="Bowl of yogurt with fresh berries"></div><h4>Ginger helps you make</h4><div class="date">Mar 17, 2016</div><div class="meta"><i>♥</i> 914 &nbsp; <i>●</i> 8 &nbsp; <i>♥</i> 4</div><span class="btn-outline">READ THE ARTICLE</span></article>
  <article class="abs article" style="left:462px"><div class="art" style="background:linear-gradient(135deg,#3e5a2e,#b0784a 55%,#6f8f3a)" role="img" aria-label="Woman eating fresh greens"></div><h4>Organic fruits and</h4><div class="date">Mar 17, 2016</div><div class="meta"><i>♥</i> 1072 &nbsp; <i>●</i> 8 &nbsp; <i>♥</i> 4</div><span class="btn-outline">READ THE ARTICLE</span></article>
  <article class="abs article" style="left:763px"><div class="art" style="background:linear-gradient(135deg,#d9c2c8,#8a4a78 55%,#5a2a4a)" role="img" aria-label="Jars of berry smoothie with blackberries"></div><h4>Add fresh and sweet</h4><div class="date">Mar 17, 2016</div><div class="meta"><i>♥</i> 1005 &nbsp; <i>●</i> 8 &nbsp; <i>♥</i> 4</div><span class="btn-outline">READ THE ARTICLE</span></article>
</section>

<section class="abs news">
  <h2>Stay in Touch with Updates</h2>
  <div class="field">Enter your email</div>
  <div class="submit">✉ SUBMIT</div>
  <div class="terms"><span></span>I have read and agree to the terms &amp; conditions</div>
</section>
<div class="abs map" role="img" aria-label="Street map showing the shop location"></div>

<footer class="footer">
  <div class="abs brand">Velno</div>
  <p class="abs footer-about">Fresh fruit picked daily and pressed to order, served clean and cool near the old harbour. Choose your fruit and we will slice, squeeze or blend it for you while you wait in the shade.</p>

  <div class="abs col-title" style="left:527px">Our Info</div>
  <ul class="abs col-list" style="left:527px"><li>Our Store</li><li>Contacts</li><li>Vacancies</li><li>Menu</li><li>Blog</li></ul>

  <div class="abs col-title" style="left:683px">Links</div>
  <ul class="abs col-list" style="left:683px"><li>Our Store</li><li>Contacts</li><li>Vacancies</li><li>Menu</li><li>Blog</li></ul>

  <div class="abs col-title" style="left:818px">Contacts</div>
  <div class="abs contact">
    <div><span class="ico">✆</span>555-210-4477</div>
    <div><span class="ico">⌖</span>14, Rosewood Lane, Harbor Bay, KL 68201</div>
    <div><span class="ico">✉</span>hello@velno.example</div>
  </div>
  <div class="abs social"><span></span><span></span><span></span><span></span></div>

  <div class="abs copy">© 2019 Velno</div>
  <div class="abs to-top"><svg width="45" height="45" viewBox="0 0 45 45"><path d="M16 26 L22.5 19 L29 26" stroke="#fff" stroke-width="2.5" fill="none"/></svg></div>
</footer>

</body>
</html>
```